quiet meadow therapy (QMT)

I need to build a website for my therapy business.
There are two parts to the website
on the landing page; they choose whether they are therapists making a referral or patients needing more information.
After that, they are taken to their respective pages.
There is the textual information and a referral form on the therapist page, and on the patient page, the text is a bit different, and there will be a booking page on the patient page.
Visually minimal, it's a therapeutic website. I want it clean, clinical, and modern
colors: greenish blue or maybe orangish
PHP/html code
Updates

Hi everyone
I'm very sorry for the lack of responses to your designs. I am trying to work it out, but this platform has been a challenge for me.
I appreciate everyone's efforts, and I am unsure how to rate designs and move forward with the ones I like. There is a 5-star rating, but I don't understand how I'm supposed to politely say that it is not it without feeling like I'm going to affect someone's future rating negatively.
Please understand me. Thank you

Designs look the same

Target Market(s)

therapy and stress management

Industry/Entity Type

stress management therapy

Coding

Coded - Design and coding required

Number of Pages Required

5+ page

Font styles to use
Serif

Colors
0094D4
00A9DD
6FCCEA
C7EBF8
E9F6FB
00AB8E
00BBA5
67D7C9
C6EFE9
E9F9F6

Requirements
Must have
• landing page that that have 2 options. one for therapist another for patient

```html
<!DOCTYPE html>
<html lang="en">
<head>
<meta charset="utf-8">
<title>Quiet Meadow Therapy</title>
<link rel="stylesheet" href="https://fonts.googleapis.com/css2?family=Fira+Sans+Condensed:wght@500;600;700&family=Poppins:wght@500;600&display=swap">
<style>
  :root {
    --teal: #17968b;
    --teal-soft: #5fb5b0;
    --teal-input: #46aca3;
    --violet: #6674ff;
    --violet-soft: #cdd0fb;
    --orange: #f7a43a;
    --ink: #222222;
    --white: #ffffff;
    --hero-text: #f1eef2;
  }
  * { box-sizing: border-box; margin: 0; padding: 0; }
  html, body { width: 1127px; height: 1200px; overflow: hidden; background: var(--white); }
  body { position: relative; font-family: "Fira Sans Condensed", "Arial Narrow", sans-serif; }

  .site-header { position: absolute; left: 0; top: 0; width: 1127px; height: 80px; }
  .brand { position: absolute; left: 113px; top: 18px; display: flex; align-items: center; gap: 12px; }
  .brand-dot { width: 30px; height: 30px; border-radius: 50%; background: var(--teal); }
  .brand-name { font-family: "Poppins", sans-serif; font-weight: 600; font-size: 30px; letter-spacing: 10px; color: var(--ink); line-height: 1; }

  .phone-button { position: absolute; left: 1016px; top: 0; width: 111px; height: 29px; background: var(--teal); border: 1px solid #8fcf9a; border-top: none; display: flex; align-items: center; justify-content: center; gap: 5px; color: var(--white); font-family: "Poppins", sans-serif; font-weight: 500; font-size: 9px; }
  .phone-button svg { width: 11px; height: 11px; }

  .hero { position: absolute; left: 0; top: 80px; width: 1127px; height: 431px; }
  .hero-photo { position: absolute; inset: 0;
    background:
      radial-gradient(ellipse 180px 60px at 380px 40px, rgba(240,150,40,.75), transparent 70%),
      radial-gradient(ellipse 300px 200px at 300px 360px, rgba(60,30,35,.85), transparent 70%),
      radial-gradient(ellipse 260px 160px at 560px 330px, rgba(210,130,80,.6), transparent 70%),
      radial-gradient(ellipse 300px 250px at 960px 200px, rgba(80,150,170,.7), transparent 70%),
      linear-gradient(180deg, #6a5670 0%, #4b3a63 40%, #5a3a4a 75%, #3a2630 100%); }
  .hero-copy { position: absolute; left: 109px; top: 100px; width: 520px; }
  .hero-title { font-weight: 700; font-size: 46px; line-height: 53px; color: var(--hero-text); text-transform: uppercase; letter-spacing: -0.5px; }
  .hero-title .highlight { background: linear-gradient(180deg, transparent 58%, var(--orange) 58%, var(--orange) 82%, transparent 82%); }
  .hero-lead { margin-top: 32px; width: 490px; font-weight: 600; font-size: 15.5px; line-height: 18px; color: var(--hero-text); }

  .choices { position: absolute; left: 0; top: 659px; width: 1127px; height: 270px; }
  .choice-back { position: absolute; top: 0; height: 264px; }
  .choice-card { position: absolute; top: 19px; width: 455px; height: 226px; text-align: center; color: var(--white); box-shadow: 0 2px 4px rgba(0,0,0,.2); padding-top: 36px; }
  .choice-title { font-weight: 700; font-size: 40px; line-height: 44px; text-transform: uppercase; }
  .choice-text { margin: 14px auto 0; width: 330px; font-weight: 600; font-size: 15px; line-height: 18px; }
  .choice-arrow { display: block; margin: 24px auto 0; width: 70px; height: 34px; }

  .referral-back { left: 78px; width: 413px; background: var(--teal-soft); }
  .referral-card { left: 100px; background: var(--teal); }
  .patient-back { left: 630px; width: 426px; background: var(--violet-soft); box-shadow: 0 2px 3px rgba(0,0,0,.15); }
  .patient-card { left: 578px; background: var(--violet); }

  .site-footer { position: absolute; left: 0; top: 1116px; width: 1127px; height: 84px; background: var(--teal); font-family: "Poppins", sans-serif; color: var(--white); }
  .copyright { position: absolute; left: 69px; top: 34px; font-weight: 600; font-size: 12px; }
  .newsletter { position: absolute; left: 785px; top: 31px; display: flex; align-items: center; gap: 18px; }
  .newsletter-label { font-weight: 600; font-size: 12px; }
  .newsletter-input { width: 164px; height: 25px; border-radius: 13px; border: 1px solid var(--white); background: var(--teal-input); color: var(--white); font-family: "Poppins", sans-serif; font-size: 7px; padding-left: 11px; display: flex; align-items: center; }
</style>
</head>
<body>
  <header class="site-header">
    <div class="brand">
      <span class="brand-dot"></span>
      <span class="brand-name">QMT</span>
    </div>
    <div class="phone-button">
      <svg viewBox="0 0 24 24" fill="none" stroke="#ffffff" stroke-width="1.6" stroke-linecap="round" stroke-linejoin="round"><path d="M22 16.9v3a2 2 0 0 1-2.2 2 19.8 19.8 0 0 1-8.6-3.1 19.5 19.5 0 0 1-6-6A19.8 19.8 0 0 1 2.1 4.2 2 2 0 0 1 4.1 2h3a2 2 0 0 1 2 1.7c.1 1 .4 1.9.7 2.8a2 2 0 0 1-.5 2.1L8 9.9a16 16 0 0 0 6 6l1.3-1.3a2 2 0 0 1 2.1-.4c.9.3 1.8.6 2.8.7a2 2 0 0 1 1.7 2z"/></svg>
      <span>0 100 200 300</span>
    </div>
  </header>

  <section class="hero">
    <div class="hero-photo" role="img" aria-label="Soft-focus photo of stacked pebbles by water at sunset"></div>
    <div class="hero-copy">
      <h1 class="hero-title"><span class="highlight">Welcome to</span><br>Quiet<br>Meadow Therapy</h1>
      <p class="hero-lead">Mi Vitae, At Massa, Eget Sollicitudin Nibh. Massa, Consequat Tellus Risus Ut Adipiscing.</p>
    </div>
  </section>

  <section class="choices">
    <div class="choice-back referral-back"></div>
    <div class="choice-card referral-card">
      <h2 class="choice-title">Make a Referral</h2>
      <p class="choice-text">Mi Vitae, At Massa, Eget Sollicitudin Nibh. Massa, Consequat Tellus Risus Ut Adipiscing.</p>
      <svg class="choice-arrow" viewBox="0 0 70 34" fill="none" stroke="#ffffff" stroke-width="1"><line x1="1" y1="17" x2="52" y2="17"/><circle cx="52" cy="17" r="16"/><polyline points="47,10 54,17 47,24"/></svg>
    </div>
    <div class="choice-back patient-back"></div>
    <div class="choice-card patient-card">
      <h2 class="choice-title">Patient Page</h2>
      <p class="choice-text">Mi Vitae, At Massa, Eget Sollicitudin Nibh. Massa, Consequat Tellus Risus Ut Adipiscing.</p>
      <svg class="choice-arrow" viewBox="0 0 70 34" fill="none" stroke="#ffffff" stroke-width="1"><line x1="1" y1="17" x2="52" y2="17"/><circle cx="52" cy="17" r="16"/><polyline points="47,10 54,17 47,24"/></svg>
    </div>
  </section>

  <footer class="site-footer">
    <p class="copyright">Copyright @2022 All Rights Reserved</p>
    <div class="newsletter">
      <span class="newsletter-label">Subscribe To Newsletter</span>
      <div class="newsletter-input">Enter your email</div>
    </div>
  </footer>
</body>
</html>
```